New Business Card Design Project

I would like my card design to look exactly like the logo, design, layout, and print of the current attached file. The only change I would like made would be for the print to say THE KMW GROUP instead of THE HALLORAN GROUP. Basically, just replace his group name with my group name. I would also like the backgroud to be the same texture and color as the attached file. I love the dark blue lettering and house logo on the card.

I am completely open to the rest of the card design. I just want something clean and simple. Only basic contact info required on the card. Maybe just name: Kyle M Warrick and cell # 555.914.2087 and email kyle@orchidhomesagent.com

```html
<!DOCTYPE html>
<html lang="en">
<head>
<meta charset="utf-8">
<title>The KMW Group – Business Card</title>
<link rel="stylesheet" href="https://fonts.googleapis.com/css2?family=Open+Sans:wght@400;800&display=swap">
<style>
  :root {
    --navy: #23226b;
    --stock: #ebebee;
    --panel: #ffffff;
    --lilac: #c3c2d8;
    --backdrop: #f6f6f4;
  }
  * { margin: 0; padding: 0; box-sizing: border-box; }
  html, body { width: 1200px; height: 1200px; overflow: hidden; }
  body {
    background: var(--backdrop);
    font-family: "Open Sans", Arial, sans-serif;
    color: var(--navy);
    display: flex;
    flex-direction: column;
    align-items: center;
    justify-content: center;
    gap: 52px;
  }
  .card {
    position: relative;
    width: 900px;
    height: 514px;
    background: var(--stock);
    box-shadow: 0 2px 6px rgba(0,0,0,0.15);
    overflow: hidden;
  }
  .brand-box {
    position: absolute;
    display: flex;
    align-items: center;
    justify-content: center;
    gap: 0.6em;
    background: var(--panel);
    border: 4px solid var(--navy);
    border-radius: 28px;
    font-weight: 400;
    letter-spacing: 0.14em;
    color: var(--navy);
    white-space: nowrap;
  }
  .brand-mark {
    width: 0.9em;
    height: 0.9em;
    background: var(--navy);
  }
  .card--front .brand-box {
    left: 150px; top: 122px;
    width: 600px; height: 270px;
    font-size: 44px;
  }
  .card--back .brand-box {
    left: 150px; top: 318px;
    width: 300px; height: 140px;
    font-size: 22px;
    border-width: 3px;
    border-radius: 18px;
  }
  .accent {
    position: absolute;
    right: 0; top: 0;
    width: 330px; height: 300px;
    background: radial-gradient(ellipse at 75% 20%, var(--lilac) 0%, var(--lilac) 45%, rgba(195,194,216,0) 72%);
  }
  .holder-name {
    position: absolute;
    left: 64px; top: 150px;
    font-size: 50px;
    font-weight: 800;
    letter-spacing: 0.22em;
    white-space: nowrap;
  }
  .contact {
    position: absolute;
    left: 480px; top: 262px;
    list-style: none;
    font-size: 28px;
    letter-spacing: 0.04em;
  }
  .contact li {
    display: flex;
    align-items: center;
    gap: 12px;
    margin-bottom: 14px;
    white-space: nowrap;
  }
  .contact svg { width: 26px; height: 26px; flex: none; fill: var(--navy); }
  .contact .email { font-size: 23px; letter-spacing: 0.02em; }
</style>
</head>
<body>
  <section class="card card--front">
    <div class="brand-box"><span class="brand-mark"></span>THE KMW GROUP</div>
  </section>

  <section class="card card--back">
    <div class="accent" role="img" aria-label="Soft lilac abstract blob shapes in the top-right corner"></div>
    <h1 class="holder-name">KYLE M WARRICK</h1>
    <ul class="contact">
      <li>
        <svg viewBox="0 0 24 24" aria-hidden="true"><path d="M6.6 10.8a15.1 15.1 0 0 0 6.6 6.6l2.2-2.2c.3-.3.7-.4 1-.2 1.1.4 2.3.6 3.6.6.6 0 1 .4 1 1V20c0 .6-.4 1-1 1A17 17 0 0 1 3 4c0-.6.4-1 1-1h3.5c.6 0 1 .4 1 1 0 1.3.2 2.5.6 3.6.1.3 0 .7-.2 1z"/></svg>
        <span>555.914.2087</span>
      </li>
      <li class="email">
        <svg viewBox="0 0 24 24" aria-hidden="true"><path d="M2 5h20v14H2zM3.5 6.5 12 13l8.5-6.5z" fill-rule="evenodd"/></svg>
        <span>kyle@orchidhomesagent.com</span>
      </li>
    </ul>
    <div class="brand-box"><span class="brand-mark"></span>THE KMW GROUP</div>
  </section>
</body>
</html>
```